Simple elegant business card

General card for a fin and television director.
Just want name, email, phone and address.

Target Market(s)

Prospective employers

Industry/Entity Type

Business

Requirements
Must have
• As above
Nice to have
• Logo but not necessary.
Should not have
• Not too colourful or funky.
• Simplicity and elegance the way to go.

```html
<!DOCTYPE html>
<html lang="en">
<head>
<meta charset="utf-8">
<title>Nora Vale — Business Card</title>
<link href="https://fonts.googleapis.com/css2?family=Quicksand:wght@400;500&display=swap" rel="stylesheet">
<style>
  :root {
    --page-bg: #e9e7e4;
    --card-bg: #fbfbfa;
    --ink: #2b2b2b;
    --ink-soft: #3a3a3a;
  }
  * { margin: 0; padding: 0; box-sizing: border-box; }
  html, body {
    width: 1200px;
    height: 1000px;
    overflow: hidden;
    background: var(--page-bg);
  }
  .canvas {
    position: relative;
    width: 1200px;
    height: 1000px;
  }
  .card {
    position: absolute;
    left: 150px;
    top: 243px;
    width: 900px;
    height: 514px;
    background: var(--card-bg);
    box-shadow: 0 6px 18px rgba(0, 0, 0, 0.12);
    font-family: "Quicksand", sans-serif;
    color: var(--ink);
  }
  .identity {
    position: absolute;
    left: 50%;
    top: 176px;
    transform: translateX(-50%);
    display: flex;
    flex-direction: column;
    align-items: flex-end;
  }
  .identity__name {
    font-weight: 400;
    font-size: 56px;
    letter-spacing: 3px;
    line-height: 1;
    white-space: nowrap;
  }
  .identity__role {
    margin-top: 8px;
    font-weight: 500;
    font-style: italic;
    font-size: 20px;
    letter-spacing: 2px;
    color: var(--ink-soft);
    white-space: nowrap;
  }
  .contact {
    position: absolute;
    left: 0;
    right: 0;
    bottom: 40px;
    display: flex;
    justify-content: center;
    gap: 30px;
    font-size: 21px;
    font-weight: 500;
    letter-spacing: 0.5px;
    color: var(--ink-soft);
  }
  .contact__item {
    display: flex;
    align-items: center;
    gap: 8px;
  }
  .contact__icon {
    width: 18px;
    height: 18px;
    fill: var(--ink-soft);
  }
</style>
</head>
<body>
<main class="canvas">
  <section class="card" aria-label="Business card front">
    <div class="identity">
      <h1 class="identity__name">NORA VALE</h1>
      <p class="identity__role">FILM &amp; TV DIRECTOR</p>
    </div>
    <footer class="contact">
      <span class="contact__item">
        <svg class="contact__icon" viewBox="0 0 24 24" aria-hidden="true">
          <path d="M6.6 2.5c.6-.3 1.3-.1 1.6.5l2 3.6c.3.6.2 1.2-.3 1.6l-1.5 1.2c.9 2 2.5 3.7 4.5 4.7l1.2-1.5c.4-.5 1.1-.6 1.6-.3l3.6 2c.6.3.8 1 .5 1.6l-1 2.1c-.4.8-1.3 1.2-2.2 1C9.9 17.7 5.4 13.2 4.1 6.6c-.2-.9.2-1.8 1-2.2z"/>
        </svg>
        +1 555 014 2286
      </span>
      <span class="contact__item">
        <svg class="contact__icon" viewBox="0 0 24 24" aria-hidden="true">
          <path d="M2 5h20v14H2z M3.5 6.5 12 12.5l8.5-6z" fill-rule="evenodd"/>
        </svg>
        noravale@mail.com
      </span>
    </footer>
  </section>
</main>
</body>
</html>
```